Deactivated Coal-Fired Power Plant to be redeveloped into a Green Energy Campus.

Want a striking business card statement that introduces our concept project to provide economic and community recovery to a former rural coal community in western PA.
Essentially 12 project representatives that will lead both the demolition of an existing power plant and the redevelopment to a new Green energy site.
Business Card should reflect our effort.
We are open to ideas.

Target Market(s)

Energy and Power Generation industries

Industry/Entity Type

Power Generation and Data Centers

Contact Information for Business Card

Included in uploaded materials

Font styles to use
Sans Serif
Other font styles liked:
• Arial, Calibri

Requirements
Must have
• Multiple colors

```html
<!DOCTYPE html>
<html lang="en">
<head>
<meta charset="utf-8">
<title>Ridgeline Renewal – Business Card</title>
<link href="https://fonts.googleapis.com/css2?family=Arimo:wght@400;700&display=swap" rel="stylesheet">
<style>
  :root {
    --canvas: #e4e5e7;
    --card-dark: #050505;
    --card-light: #f7f7f7;
    --green: #169447;
    --ink: #111111;
    --white: #ffffff;
    --rule: #8a8a8a;
  }
  * { margin: 0; padding: 0; box-sizing: border-box; }
  html, body {
    width: 1200px; height: 800px; overflow: hidden;
    background: var(--canvas);
    font-family: "Arimo", Arial, sans-serif;
  }
  .canvas { position: relative; width: 1200px; height: 800px; }
  .card {
    position: absolute; top: 246px;
    width: 540px; height: 308px;
    border-radius: 22px; overflow: hidden;
  }
  .card--back { left: 40px; background: var(--card-dark); color: var(--white); }
  .card--front { left: 620px; background: var(--card-light); color: var(--ink); }

  /* back */
  .brand-corner {
    position: absolute; top: 40px; right: 40px;
    display: flex; align-items: center; gap: 10px;
  }
  .brand-corner .dot { width: 58px; height: 58px; border-radius: 50%; background: var(--green); }
  .brand-corner .brand-name { font-weight: 700; font-size: 15px; color: var(--white); letter-spacing: .5px; }
  .person { position: absolute; left: 36px; top: 168px; }
  .person__name { font-weight: 700; font-size: 22px; letter-spacing: .3px; }
  .person__title { font-size: 14px; color: var(--green); margin-top: 3px; }
  .divider {
    position: absolute; left: 36px; right: 36px; top: 222px;
    height: 1px; background: var(--rule);
  }
  .contact { position: absolute; left: 36px; top: 234px; font-size: 13px; line-height: 18px; }
  .company { position: absolute; right: 36px; top: 234px; text-align: right; font-size: 13px; line-height: 18px; }

  /* front */
  .lockup {
    position: absolute; left: 0; right: 0; top: 100px;
    display: flex; align-items: center; justify-content: center; gap: 14px;
  }
  .lockup .dot { width: 64px; height: 64px; border-radius: 50%; background: var(--green); }
  .lockup .brand-name { font-weight: 700; font-size: 34px; color: var(--ink); letter-spacing: .5px; }
  .tagline {
    position: absolute; left: 0; right: 0; top: 214px;
    text-align: center; font-size: 14px; letter-spacing: 3px; color: #333;
  }
</style>
</head>
<body>
<main class="canvas">
  <section class="card card--back" aria-label="Business card back">
    <div class="brand-corner">
      <span class="dot"></span>
      <span class="brand-name">Ridgeline Renewal</span>
    </div>
    <div class="person">
      <p class="person__name">Daniel Hartwell</p>
      <p class="person__title">Chief Operation Officer</p>
    </div>
    <div class="divider"></div>
    <div class="contact">
      <p>555.214.3080</p>
      <p>dhartwell@ridgelinerenewal.com</p>
    </div>
    <div class="company">
      <p>Ridgeline Renewal LLC</p>
      <p>ridgelinerenewal.com</p>
    </div>
  </section>

  <section class="card card--front" aria-label="Business card front">
    <div class="lockup">
      <span class="dot"></span>
      <span class="brand-name">Ridgeline Renewal</span>
    </div>
    <p class="tagline">Your Tagline Here</p>
  </section>
</main>
</body>
</html>
```